Garnett and Lyle Personal Injury Billboard

We'd like a clean/modern billboard to build brand awareness for our law firm in the area of personal injury. Ideally, we like the word "Injured?" or something similar in large lettering.

I'm attaching images, logo and award badges which could be used. The billboards will be 14x48 ft and 10.6x36.

We are open to different color ideas, fonts, and artwork. Creative but not too busy with wording. Our web page is www.kgarnettfirm.example

Garnett & Lyle Law Firm
(555) 318-4092

```html
<!DOCTYPE html>
<html lang="en">
<head>
<meta charset="UTF-8">
<title>Garnett &amp; Lyle Law Firm – Personal Injury Billboard</title>
<link href="https://fonts.googleapis.com/css2?family=Montserrat:wght@500;700;800;900&display=swap" rel="stylesheet">
<style>
  :root {
    --navy-deep: #0c1a33;
    --navy: #14305a;
    --blue: #1f4f8c;
    --blue-bright: #2d6bb5;
    --white: #ffffff;
    --paper: #eceef1;
    --ink: #151515;
    --rule: #9fb3cc;
    --badge: #36a3dc;
    --stage: #e6e9ee;
  }
  * { margin: 0; padding: 0; box-sizing: border-box; }
  html, body {
    width: 1200px; height: 970px; overflow: hidden;
    background: var(--stage);
    font-family: "Montserrat", Arial, sans-serif;
  }
  .billboard {
    position: absolute; left: 30px; top: 318px;
    width: 1140px; height: 333px; overflow: hidden;
    background: radial-gradient(ellipse at 30% 55%, var(--blue-bright) 0%, var(--blue) 28%, var(--navy) 58%, var(--navy-deep) 100%);
  }
  .headline {
    position: absolute; left: 28px; top: 28px;
    font-size: 76px; font-weight: 900; letter-spacing: -1px;
    color: var(--white); line-height: 1;
  }
  .call-row {
    position: absolute; left: 28px; top: 118px; width: 410px; height: 36px;
    display: flex; align-items: center; gap: 14px;
  }
  .call-row .rule { flex: 1; height: 1.5px; background: var(--rule); }
  .call-row svg { width: 34px; height: 34px; }
  .phone {
    position: absolute; left: 26px; top: 162px;
    font-size: 58px; font-weight: 800; letter-spacing: -1px;
    color: var(--white); line-height: 1;
  }
  .name-band {
    position: absolute; left: 0; bottom: 0; width: 460px; height: 66px;
    background: var(--paper);
    display: flex; align-items: center; padding-left: 28px; gap: 10px;
    font-size: 28px; line-height: 1;
  }
  .name-band .firm { font-weight: 800; color: var(--ink); }
  .name-band .suffix {
    font-weight: 800; color: transparent;
    -webkit-text-stroke: 1.2px var(--ink);
  }
  .portrait {
    position: absolute; left: 460px; top: 70px; width: 330px; height: 263px;
    background: linear-gradient(180deg, #9a8f88 0%, #7c7b80 45%, #4f5562 100%);
  }
  .statue {
    position: absolute; left: 790px; top: 70px; width: 120px; height: 160px;
    background: radial-gradient(ellipse at 50% 45%, rgba(90,120,165,0.45) 0%, rgba(20,48,90,0) 70%);
  }
  .logo {
    position: absolute; left: 880px; top: 38px;
    display: flex; align-items: center; gap: 12px;
  }
  .logo .mark { width: 16px; height: 16px; background: var(--white); }
  .logo .wordmark {
    font-size: 20px; font-weight: 700; color: var(--white);
    line-height: 1.15; letter-spacing: 0.5px;
  }
  .award {
    position: absolute; left: 960px; top: 122px; width: 96px; height: 108px;
    background: var(--badge);
    border: 3px solid var(--white);
  }
  .web-band {
    position: absolute; right: 0; bottom: 0; width: 350px; height: 100px;
    background: var(--paper);
    display: flex; align-items: center; justify-content: center;
  }
  .web-band .url {
    font-size: 19px; font-weight: 800; color: var(--navy);
    padding-bottom: 4px; border-bottom: 2px solid var(--blue);
  }
</style>
</head>
<body>
  <section class="billboard">
    <h1 class="headline">INJURED?</h1>
    <div class="call-row">
      <span class="rule"></span>
      <svg viewBox="0 0 34 34" aria-hidden="true">
        <path d="M8 6 L13 6 L15 12 L12 14 C13.5 18 16 20.5 20 22 L22 19 L28 21 L28 26 C28 27.5 27 28.5 25.5 28.5 C15 28 6 19 5.5 8.5 C5.5 7 6.5 6 8 6 Z" fill="#ffffff"/>
        <path d="M20 10 A5 5 0 0 1 24 14" stroke="#ffffff" stroke-width="2" fill="none" stroke-linecap="round"/>
        <path d="M21 5 A10 10 0 0 1 29 13" stroke="#ffffff" stroke-width="2" fill="none" stroke-linecap="round"/>
      </svg>
      <span class="rule"></span>
    </div>
    <p class="phone">555-318-4092</p>
    <div class="name-band">
      <span class="firm">GARNETT &amp; LYLE</span>
      <span class="suffix">LAW FIRM</span>
    </div>

    <div class="portrait" role="img" aria-label="Photo of the firm's two attorneys in suits, smiling"></div>
    <div class="statue" role="img" aria-label="Faint image of a Lady Justice statue"></div>

    <div class="logo">
      <span class="mark"></span>
      <span class="wordmark">Garnett &amp; Lyle<br>Law Firm PLLC</span>
    </div>
    <div class="award" role="img" aria-label="2023 community choice award badge"></div>

    <div class="web-band">
      <span class="url">KGARNETTFIRM.EXAMPLE</span>
    </div>
  </section>
</body>
</html>
```